Design some Business Cards for Garbage Collection company

We are a garbage collection company that is seeking a design for Magnetic Cards to be placed on our residential customer fridges. The primary goal of the Magnetic card is to inform our Customers of when their garbage collection day is e.g " Your Garbage Collection Day is Monday" (See attached image). Also, on the card we will like to advertise our other services which is Septic Tank Emptying, Portable Toilet Rental, and Skip Bin Rental.

We are looking for fun design that people would not throw away and that would look good on their fridge.

Our Contact Information:

Dralith Waste Management
318 Heron Crescent
North Palmvale Heights
Georgetown
Guyana
(592) 304-7729 or (592) 304-6382

Any additional info please feel free to ask

```html
<!DOCTYPE html>
<html lang="en">
<head>
<meta charset="utf-8">
<title>Dralith Waste Management – Business Card</title>
<link href="https://fonts.googleapis.com/css2?family=Arimo:wght@400;700&family=Tinos:wght@700&display=swap" rel="stylesheet">
<style>
  :root {
    --page: #e9e9e9;
    --card: #ffffff;
    --ink: #2b2b2b;
    --muted: #555555;
    --red: #e0413f;
    --red-band: #e25552;
    --green: #5bb143;
    --yellow: #f2d43a;
  }
  * { box-sizing: border-box; margin: 0; padding: 0; }
  html, body { width: 1200px; height: 897px; overflow: hidden; }
  body {
    background: var(--page);
    font-family: "Arimo", Arial, sans-serif;
    color: var(--ink);
    position: relative;
  }
  .card {
    position: absolute;
    left: 100px; top: 163px;
    width: 1000px; height: 571px;
    background: var(--card);
    box-shadow: 0 6px 24px rgba(0,0,0,.15);
    overflow: hidden;
  }
  .card-bands { position: absolute; inset: 0; width: 100%; height: 100%; }
  .holder { position: absolute; left: 70px; top: 70px; }
  .holder-name { font-size: 32px; color: var(--muted); }
  .holder-title { font-size: 20px; font-weight: 700; color: var(--red); margin-top: 4px; }
  .contacts { position: absolute; left: 70px; top: 195px; list-style: none; }
  .contacts li { display: flex; align-items: center; gap: 14px; font-size: 23px; color: var(--muted); line-height: 36px; }
  .contacts svg { width: 20px; height: 20px; fill: var(--red); flex: none; }
  .services { position: absolute; left: 70px; top: 350px; }
  .services-title { font-size: 23px; color: var(--red); margin-bottom: 4px; }
  .services li { list-style: none; font-size: 25px; color: var(--ink); line-height: 34px; }
  .brand { position: absolute; left: 560px; top: 38px; width: 330px; text-align: center; }
  .brand-mark { display: inline-flex; align-items: center; gap: 12px; }
  .brand-dot { width: 40px; height: 40px; border-radius: 50%; background: var(--green); }
  .brand-name { font-size: 34px; font-weight: 700; color: var(--green); }
  .tagline { font-family: "Tinos", "Times New Roman", serif; font-weight: 700; font-size: 19px; margin-top: 14px; }
  .collection { margin-top: 12px; font-size: 21px; color: var(--muted); }
  .collection-day { font-size: 24px; font-weight: 700; color: var(--red); margin-top: 6px; }
  .address { position: absolute; left: 600px; top: 290px; font-size: 21px; color: var(--muted); line-height: 30px; }
  .address-company { color: var(--red); font-size: 22px; }
</style>
</head>
<body>
  <section class="card">
    <svg class="card-bands" viewBox="0 0 1000 571" preserveAspectRatio="none" aria-hidden="true">
      <polygon points="610,438 1000,438 1000,450 598,450" fill="var(--green)"/>
      <polygon points="0,500 560,500 600,462 1000,462 1000,571 0,571" fill="var(--red-band)"/>
    </svg>

    <div class="holder">
      <p class="holder-name">Marlon Tervick</p>
      <p class="holder-title">President</p>
    </div>

    <ul class="contacts">
      <li><svg viewBox="0 0 24 24"><path d="M6.6 10.8a15 15 0 0 0 6.6 6.6l2.2-2.2a1 1 0 0 1 1-.25 11.4 11.4 0 0 0 3.6.57 1 1 0 0 1 1 1V20a1 1 0 0 1-1 1A17 17 0 0 1 3 4a1 1 0 0 1 1-1h3.5a1 1 0 0 1 1 1c0 1.25.2 2.45.57 3.57a1 1 0 0 1-.25 1z"/></svg>(592) 304-7729</li>
      <li><svg viewBox="0 0 24 24"><path d="M3 8c0-2 4-4 9-4s9 2 9 4v2h-5V8H8v2H3zM6 12h12l2 8H4zm6 2a2 2 0 1 0 0 4 2 2 0 0 0 0-4z"/></svg>(592) 304-6382</li>
      <li><svg viewBox="0 0 24 24"><path d="M2 5h20v14H2zm2 2v.5l8 5 8-5V7zm0 2.8V17h16V9.8l-8 5z"/></svg>info@dralith.com</li>
      <li><svg viewBox="0 0 24 24"><circle cx="12" cy="12" r="10"/></svg>www.dralith.com</li>
    </ul>

    <div class="services">
      <p class="services-title">Other Services:</p>
      <ul>
        <li>Septic Tank Emptying</li>
        <li>Portable Toilet Rental</li>
        <li>Skip Bin Rental.</li>
      </ul>
    </div>

    <div class="brand">
      <div class="brand-mark"><span class="brand-dot"></span><span class="brand-name">Dralith</span></div>
      <p class="tagline">Moving Guyana's Waste</p>
      <p class="collection">Your Garbage Collection Day is</p>
      <p class="collection-day">MONDAY</p>
    </div>

    <address class="address" style="font-style:normal">
      <div class="address-company">Dralith Waste Management</div>
      <div>318 Heron Crescent</div>
      <div>North Palmvale Heights</div>
      <div>Georgetown, Guyana</div>
    </address>
  </section>
</body>
</html>
```